Holvik Cabinets Quality Custom Built Kitchens, Vanity Units, Robes ect

Hi,
Was after a new design for our business cards,
we are a cabinet making business and pride ourselves in quality custom built Kitchens, Vanity units, robes ect.
we have been around for over 20 years and we are trying to modernize our card logo.
Looking for something eye catching, bold and exciting
family ran and operated business, we work with builders and also have a large private clientel.

Thanks

Industry/Entity Type

Business

Contact Information for Business Card

Holvik Cabinets

Font styles to use
Serif
Script

Requirements
Must have
• Corinne 0461735928 hvcabinets@mailvane.com
• Po Box 2786
• 5B Wattlebark Court Traralgon Vic 3844
• Phone (03)59286417 Fax (03) 59286942
Nice to have
• Quality Custom Built Kitchens & Vanity Units

```html
<!DOCTYPE html>
<html lang="en">
<head>
<meta charset="utf-8">
<title>Holvik Cabinets – Business Card</title>
<link href="https://fonts.googleapis.com/css2?family=Marcellus&family=Great+Vibes&family=Arimo&display=swap" rel="stylesheet">
<style>
  :root {
    --navy: #1c4560;
    --yellow: #e6e000;
    --white: #ffffff;
    --label: #231f20;
  }
  html, body {
    margin: 0;
    padding: 0;
    width: 1200px;
    height: 1196px;
    overflow: hidden;
    background: var(--white);
  }
  .sheet { display: block; width: 1200px; height: 1196px; }
  .side-label { font-family: "Arimo", Arial, sans-serif; font-size: 35px; fill: var(--label); }
  .brand-text { font-family: "Marcellus", Georgia, serif; font-weight: 400; }
  .script-text { font-family: "Great Vibes", "Brush Script MT", cursive; font-weight: 400; }
  .contact-name, .contact-mobile, .contact-email, .contact-pobox, .brand-name, .brand-tagline { fill: var(--navy); }
  .contact-name { font-size: 50px; }
  .contact-mobile { font-size: 40px; }
  .contact-email { font-size: 30px; }
  .contact-pobox { font-size: 30px; }
  .brand-name { font-size: 72px; }
  .brand-tagline { font-size: 36px; }
  .office-details { font-size: 30px; fill: var(--white); }
  .back-name { font-size: 64px; fill: var(--white); }
  .back-tagline { font-size: 52px; fill: var(--yellow); }
</style>
</head>
<body>
<svg class="sheet" viewBox="0 0 1200 1196" xmlns="http://www.w3.org/2000/svg">
  <text class="side-label" x="563" y="36" text-anchor="middle">Front Side</text>
  <g class="card-front">
    <rect x="123" y="63" width="944" height="524" fill="var(--white)" stroke="var(--navy)" stroke-width="2"/>
    <text class="script-text contact-name" x="145" y="119" textLength="160" lengthAdjust="spacingAndGlyphs">Corinne</text>
    <text class="brand-text contact-pobox" x="145" y="163" textLength="190" lengthAdjust="spacingAndGlyphs">Po Box 2786</text>
    <text class="brand-text contact-mobile" x="769" y="117" textLength="276" lengthAdjust="spacingAndGlyphs">0461 73 5928</text>
    <text class="brand-text contact-email" x="603" y="163" textLength="442" lengthAdjust="spacingAndGlyphs">hvcabinets@mailvane.com</text>
    <text class="brand-text brand-name" x="287" y="324" textLength="616" lengthAdjust="spacingAndGlyphs">Holvik Cabinets</text>
    <text class="brand-text brand-tagline" x="171" y="382" textLength="849" lengthAdjust="spacingAndGlyphs">Quality Custom Built Kitchens &amp; Vanity Units</text>
    <rect class="office-band" x="122" y="488" width="946" height="100" fill="var(--navy)"/>
    <text class="brand-text office-details" x="231" y="526" textLength="723" lengthAdjust="spacingAndGlyphs">Ph No. (03)59286417, Fax No. (03)59286942,</text>
    <text class="brand-text office-details" x="270" y="569" textLength="646" lengthAdjust="spacingAndGlyphs">5B Wattlebark Court Traralgon Vic 3844</text>
  </g>

  <text class="side-label" x="561" y="648" text-anchor="middle">Back Side</text>
  <g class="card-back">
    <rect x="140" y="672" width="945" height="524" fill="var(--navy)"/>
    <text class="brand-text back-name" x="354" y="868" textLength="513" lengthAdjust="spacingAndGlyphs">Holvik Cabinets</text>
    <line x1="356" y1="878" x2="873" y2="878" stroke="var(--white)" stroke-width="3"/>
    <text class="brand-text back-tagline" x="202" y="942" textLength="831" lengthAdjust="spacingAndGlyphs">Quality Custom Built Kitchens</text>
    <text class="brand-text back-tagline" x="625" y="1013" text-anchor="middle">&amp;</text>
    <text class="brand-text back-tagline" x="463" y="1085" textLength="326" lengthAdjust="spacingAndGlyphs">Vanity Units</text>
  </g>
</svg>
</body>
</html>
```